New florist business website design

Number 1 want is an easy to navigate & check out website
Needs to be beautiful and eye catching as well.
This is an online only business (no shop front)
Rustic and blush pinks, neutrals, woods, leaves
Customers need to be able to go onto my website, select something they want to buy but have the option to use a drop down box to change colours of the flowers, or add notes to make changes to the arrangement

Industry/Entity Type

Florist

Coding

Coded - Design and coding required

Number of Pages Required

5+ page

Colors
f9d9e8
fff2ec
fffefc

Requirements
Must have
• Drop down menu to take you to other pages for Arrangements, bouquets, everlasting arrangements, gifts, contact
Be able to purchase and “add to basket”
Checkout page
Nice to have
• Be able to add my own photos once I’ve taken new ones
Should not have
• Tacky images or clip art

```html
<!DOCTYPE html>
<html lang="en">
<head>
<meta charset="utf-8">
<title>Bloom &amp; Briar — Florist</title>
<link href="https://fonts.googleapis.com/css2?family=Dancing+Script:wght@500;700&family=Open+Sans:wght@400;600;700&family=Oswald:wght@400;500&display=swap" rel="stylesheet">
<style>
:root{
  --page:#fff2ec;
  --paper:#fffefc;
  --blush:#f9d9e8;
  --rose:#f07a92;
  --rose-soft:#f8c9d8;
  --peach:#fae3cc;
  --ink:#2b2b2b;
  --muted:#5d5d5d;
  --line:#d9cfc9;
  --dark:#3b3b3b;
}
*{box-sizing:border-box;margin:0;padding:0}
html,body{width:1200px;height:4054px;overflow:hidden}
body{position:relative;background:var(--page);font-family:"Open Sans",sans-serif;color:var(--ink)}
.abs{position:absolute}
.script{font-family:"Dancing Script",cursive;font-weight:500}
.sprig{position:absolute;height:28px;width:150px;border-radius:50%;background:linear-gradient(90deg,transparent,#e4d6cf,transparent)}

/* header */
.site-header{position:absolute;left:0;top:0;width:1200px;height:142px;background:var(--page)}
.brand{position:absolute;left:133px;top:-14px;width:200px;height:200px;border-radius:50%;background:var(--blush);display:flex;align-items:center;justify-content:center;z-index:3}
.brand span{font-family:"Open Sans",sans-serif;font-size:24px;font-weight:400;color:var(--dark)}
.search{position:absolute;left:387px;top:28px;width:388px;height:37px;border:2px solid var(--rose);border-radius:3px;background:#fff;display:flex}
.search span{flex:1;font-size:11px;padding:9px 12px;color:#555}
.search b{width:37px;background:var(--rose);display:flex;align-items:center;justify-content:center}
.util{position:absolute;top:42px;font-size:10px;color:#444;display:flex;align-items:center;gap:6px}
.cart-count{position:absolute;left:1058px;top:32px;width:13px;height:13px;border-radius:50%;background:var(--rose);color:#fff;font-size:8px;text-align:center;line-height:13px}
.nav{position:absolute;top:92px;font-size:15px;color:#222;display:flex;align-items:center;gap:8px}

/* hero */
.hero{position:absolute;left:0;top:142px;width:1200px;height:564px;background:linear-gradient(100deg,#efc5dc 0%,#e8b0cf 55%,#dfa4c7 100%)}
.hero h1{position:absolute;left:137px;top:132px;font-size:100px;line-height:1;color:#111}
.hero p{position:absolute;left:137px;top:282px;font-size:18px;line-height:29px;color:#333;width:380px}
.btn-light{position:absolute;background:#fbe9ee;color:#222;font-size:16px;display:flex;align-items:center;justify-content:center;border-radius:3px}
.hero-photo{position:absolute;left:630px;top:15px;width:378px;height:543px;border-radius:45% 45% 30% 30%;background:radial-gradient(circle at 50% 35%,#e44a5a 0%,#d7526e 40%,#9c5a8a 70%,transparent 72%),linear-gradient(#e8b0cf,#e8b0cf)}
.dots{position:absolute;left:562px;top:516px;display:flex;gap:7px;align-items:center}
.dots i{width:6px;height:6px;border-radius:50%;background:#333}
.dots i.on{width:10px;height:10px;background:none;border:2px solid #fff}

/* section titles */
.section-title{position:absolute;width:1200px;left:0;text-align:center;font-size:40px;color:#222}

/* categories */
.cat{position:absolute;width:453px;height:277px;border-radius:3px;overflow:hidden}
.cat h3{position:absolute;left:21px;font-size:18px;font-weight:700;letter-spacing:.5px;line-height:23px;color:#fff}
.cat p{position:absolute;left:21px;font-size:12px;line-height:17px;width:240px;color:#fff}
.cat .btn-small{position:absolute;left:21px;width:93px;height:31px;background:#fff;border-radius:3px;font-size:11px;font-weight:700;display:flex;align-items:center;justify-content:center;color:#222}
.cat .shot{position:absolute;right:0;top:0;height:100%;width:60%}

/* products */
.card{position:absolute;background:#fff;border-radius:3px;text-align:center}
.card .name{position:absolute;left:0;width:100%;font-size:14px;font-weight:600;letter-spacing:.3px}
.card .price{position:absolute;left:0;width:100%;font-family:"Oswald",sans-serif;font-size:21px}
.card .price s{font-size:15px;color:#666;margin-left:6px}
.card .btn-pink{position:absolute;left:50%;transform:translateX(-50%);background:var(--rose-soft);font-size:11px;font-weight:600;border-radius:3px;display:flex;align-items:center;justify-content:center;color:#333}
.card .photo{position:absolute;left:50%;transform:translateX(-50%);border-radius:50% 50% 40% 40%}
.card .ico{position:absolute}
.badge{position:absolute;left:5px;top:17px;font-size:10px;background:#f6ece8;padding:3px 5px;color:#333}
.arrow{position:absolute;top:1818px}

.outline-btn{position:absolute;left:515px;top:2047px;width:169px;height:37px;border:1px solid #333;border-radius:5px;font-size:13px;font-weight:600;display:flex;align-items:center;justify-content:center}

/* offer */
.offer{position:absolute;left:131px;top:2318px;width:700px;height:312px;background:var(--peach)}
.offer .get{position:absolute;left:37px;top:49px;width:65px;height:40px;background:#3a3a3a;color:#fff;font-size:21px;display:flex;align-items:center;justify-content:center}
.offer .rule{position:absolute;left:37px;top:89px;width:203px;height:2px;background:#3a3a3a}
.offer h2{position:absolute;left:40px;top:100px;font-size:48px;font-weight:700;color:#333}
.offer p{position:absolute;left:41px;top:196px;width:250px;font-size:13px;line-height:20px;color:#333}
.offer .btn{position:absolute;left:39px;top:251px;width:101px;height:34px;background:var(--rose-soft);font-size:13px;border-radius:3px;display:flex;align-items:center;justify-content:center}
.offer-photo{position:absolute;left:331px;top:2181px;width:803px;height:475px;border-radius:40% 30% 35% 45%;background:radial-gradient(circle at 35% 45%,#cfd9bd 0%,#e8c9c4 30%,#f3c3bb 60%,#f0a46e 85%,transparent 88%)}

/* banner */
.banner{position:absolute;left:131px;top:3260px;width:940px;height:367px;background:linear-gradient(90deg,#f6c9d3,#fbe1e6 50%,#f6c9d3)}
.banner .side{position:absolute;top:0;height:100%;width:208px;background:linear-gradient(180deg,#e9708f,#f3a8b7 60%,#9fb07a)}
.banner h2{position:absolute;left:0;top:82px;width:940px;text-align:center;font-size:22px;font-weight:600;line-height:39px;letter-spacing:.5px;color:#222}
.banner .btn{position:absolute;left:419px;top:221px;width:134px;height:47px;background:#fff;border-radius:5px;font-size:17px;display:flex;align-items:center;justify-content:center}

/* footer */
.site-footer{position:absolute;left:0;top:3693px;width:1200px;height:361px;background:var(--paper)}
.foot-brand{position:absolute;left:118px;top:40px;width:230px;height:230px;border-radius:50%;background:#fdf1ee;display:flex;align-items:center;justify-content:center}
.foot-brand span{font-size:28px;color:var(--dark)}
.foot-col{position:absolute;top:56px;font-size:11px;color:#222}
.foot-col h4{font-size:12px;font-weight:700;margin-bottom:20px}
.foot-col li{list-style:none;line-height:20px}
.contact-row{display:flex;gap:14px;align-items:flex-start;margin-bottom:21px;line-height:14px}
.circ{width:24px;height:24px;border-radius:50%;background:#f3ece8;flex:none;display:flex;align-items:center;justify-content:center}
.foot-rule{position:absolute;left:140px;top:288px;width:934px;height:1px;background:#e4dcd7}
.copy{position:absolute;left:0;top:320px;width:1210px;text-align:center;font-size:9px;color:#222}
</style>
</head>
<body>

<header class="site-header">
  <div class="brand"><span>Bloom &amp; Briar</span></div>
  <div class="search"><span>Search</span><b><svg width="14" height="14" viewBox="0 0 14 14"><circle cx="6" cy="6" r="4.2" fill="none" stroke="#fff" stroke-width="1.8"/><line x1="9" y1="9" x2="13" y2="13" stroke="#fff" stroke-width="1.8"/></svg></b></div>
  <div class="util" style="left:798px">Login &nbsp;\ My Account</div>
  <div class="util" style="left:921px;top:36px">Wishlist <svg width="22" height="20" viewBox="0 0 24 22"><path d="M12 20S2 13.5 2 7.2A5 5 0 0 1 12 5a5 5 0 0 1 10 2.2C22 13.5 12 20 12 20z" fill="none" stroke="#333" stroke-width="1.6"/></svg></div>
  <div class="util" style="left:1010px;top:36px">CART <svg width="24" height="22" viewBox="0 0 24 22"><path d="M2 3h3l3 11h11l3-8H7" fill="none" stroke="#333" stroke-width="1.8"/><circle cx="10" cy="18" r="1.8" fill="#333"/><circle cx="18" cy="18" r="1.8" fill="#333"/></svg></div>
  <div class="cart-count">0</div>
  <nav>
    <div class="nav" style="left:387px">Arrangements <svg width="10" height="7"><path d="M1 1l4 4 4-4" fill="none" stroke="#222" stroke-width="1.5"/></svg></div>
    <div class="nav" style="left:559px">Bouquets <svg width="10" height="7"><path d="M1 1l4 4 4-4" fill="none" stroke="#222" stroke-width="1.5"/></svg></div>
    <div class="nav" style="left:682px">Everlasting Arrangements <svg width="10" height="7"><path d="M1 1l4 4 4-4" fill="none" stroke="#222" stroke-width="1.5"/></svg></div>
    <div class="nav" style="left:926px">Gifts <svg width="10" height="7"><path d="M1 1l4 4 4-4" fill="none" stroke="#222" stroke-width="1.5"/></svg></div>
    <div class="nav" style="left:1011px">Contact</div>
  </nav>
</header>

<section class="hero">
  <h1 class="script">Bouquets</h1>
  <p>Lorem Ipsum is simply dummy text of the printing and typesetting industry</p>
  <div class="btn-light" style="left:135px;top:373px;width:145px;height:57px">SHOP NOW</div>
  <div class="hero-photo" role="img" aria-label="Bouquet of red, pink and white tulips tied with green ribbon"></div>
  <div class="dots"><i></i><i></i><i class="on"></i><i></i><i></i></div>
</section>

<h2 class="section-title script" style="top:742px">Categories</h2>
<div class="sprig" style="left:525px;top:800px" role="img" aria-label="Leaf sprig ornament"></div>

<section>
  <div class="cat" style="left:139px;top:884px;background:#8b8380">
    <div class="shot" role="img" aria-label="Pink peonies in a glass vase" style="background:radial-gradient(circle at 55% 35%,#e0428a,#b8326a 40%,#8b8380 70%)"></div>
    <h3 style="top:143px">ARRANGEMENTS</h3>
    <p style="top:172px">Lorem Ipsum is simply dummy text of the printing and typesetting.</p>
    <div class="btn-small" style="top:225px">SHOP NOW</div>
  </div>
  <div class="cat" style="left:609px;top:884px;background:#e98aa0">
    <div class="shot" role="img" aria-label="Hand holding a wrapped mixed bouquet" style="background:radial-gradient(circle at 60% 40%,#d9c26a,#e07aa0 45%,#e98aa0 70%)"></div>
    <h3 style="top:143px">BOUQUETS</h3>
    <p style="top:172px">Lorem Ipsum is simply dummy text of the printing and typesetting.</p>
    <div class="btn-small" style="top:225px">SHOP NOW</div>
  </div>
  <div class="cat" style="left:139px;top:1178px;background:#f3a5ae">
    <div class="shot" role="img" aria-label="Bunch of dried everlasting flowers" style="background:radial-gradient(circle at 62% 45%,#8d4aa0,#e3b640 35%,#f3a5ae 65%)"></div>
    <h3 style="top:118px">EVERLASTING<br>ARRANGEMENTS</h3>
    <p style="top:170px">Lorem Ipsum is simply dummy text of the printing and typesetting.</p>
    <div class="btn-small" style="top:225px">SHOP NOW</div>
  </div>
  <div class="cat" style="left:609px;top:1178px;background:#b9b5b2">
    <div class="shot" role="img" aria-label="Wrapped gift box beside cream and peach roses" style="width:100%;background:radial-gradient(circle at 70% 40%,#f2d7a6,#ecc49a 30%,#c9b9a8 60%,#a8a4a1)"></div>
    <h3 style="top:142px;color:#222">GIFTS</h3>
    <p style="top:172px;color:#222">Lorem Ipsum is simply dummy text of the printing and typesetting.</p>
    <div class="btn-small" style="top:225px">SHOP NOW</div>
  </div>
</section>

<h2 class="section-title script" style="top:1512px">Our Products</h2>
<div class="sprig" style="left:525px;top:1570px" role="img" aria-label="Leaf sprig ornament"></div>

<svg class="arrow" style="left:43px" width="38" height="24" viewBox="0 0 38 24"><path d="M36 12H3M12 3L3 12l9 9" fill="none" stroke="#999" stroke-width="1.6"/></svg>
<svg class="arrow" style="left:1113px" width="38" height="24" viewBox="0 0 38 24"><path d="M2 12h33M26 3l9 9-9 9" fill="none" stroke="#999" stroke-width="1.6"/></svg>

<section>
  <!-- product card template repeated -->
  <div class="card" style="left:121px;top:1655px;width:225px;height:348px">
    <svg class="ico" style="left:18px;top:16px" width="18" height="16" viewBox="0 0 24 22"><path d="M12 20S2 13.5 2 7.2A5 5 0 0 1 12 5a5 5 0 0 1 10 2.2C22 13.5 12 20 12 20z" fill="none" stroke="#444" stroke-width="1.8"/></svg>
    <svg class="ico" style="left:192px;top:15px" width="20" height="18" viewBox="0 0 24 22"><path d="M2 3h3l3 11h11l3-8H7" fill="none" stroke="#444" stroke-width="1.8"/><circle cx="10" cy="18" r="1.8" fill="#444"/><circle cx="18" cy="18" r="1.8" fill="#444"/></svg>
    <div class="photo" role="img" aria-label="Burgundy and pink rose bouquet" style="top:45px;width:185px;height:135px;background:radial-gradient(circle,#a8264a,#e08aa0 55%,#fff 75%)"></div>
    <div class="name" style="top:209px">LOREM IPSUM</div>
    <div class="price" style="top:238px">$25.99</div>
    <div class="btn-pink" style="top:282px;width:80px;height:32px">BUY NOW</div>
  </div>
  <div class="card" style="left:369px;top:1655px;width:225px;height:348px">
    <svg class="ico" style="left:18px;top:16px" width="18" height="16" viewBox="0 0 24 22"><path d="M12 20S2 13.5 2 7.2A5 5 0 0 1 12 5a5 5 0 0 1 10 2.2C22 13.5 12 20 12 20z" fill="none" stroke="#444" stroke-width="1.8"/></svg>
    <svg class="ico" style="left:192px;top:15px" width="20" height="18" viewBox="0 0 24 22"><path d="M2 3h3l3 11h11l3-8H7" fill="none" stroke="#444" stroke-width="1.8"/><circle cx="10" cy="18" r="1.8" fill="#444"/><circle cx="18" cy="18" r="1.8" fill="#444"/></svg>
    <div class="photo" role="img" aria-label="Red rose bouquet" style="top:40px;width:110px;height:150px;background:radial-gradient(circle at 50% 30%,#d3101e,#c4202c 40%,#3d6a2a 62%,#fff 75%)"></div>
    <div class="name" style="top:209px">LOREM IPSUM</div>
    <div class="price" style="top:238px">$25.99</div>
    <div class="btn-pink" style="top:282px;width:80px;height:32px">BUY NOW</div>
  </div>
  <div class="card" style="left:614px;top:1655px;width:225px;height:348px">
    <svg class="ico" style="left:18px;top:16px" width="18" height="16" viewBox="0 0 24 22"><path d="M12 20S2 13.5 2 7.2A5 5 0 0 1 12 5a5 5 0 0 1 10 2.2C22 13.5 12 20 12 20z" fill="none" stroke="#444" stroke-width="1.8"/></svg>
    <svg class="ico" style="left:192px;top:15px" width="20" height="18" viewBox="0 0 24 22"><path d="M2 3h3l3 11h11l3-8H7" fill="none" stroke="#444" stroke-width="1.8"/><circle cx="10" cy="18" r="1.8" fill="#444"/><circle cx="18" cy="18" r="1.8" fill="#444"/></svg>
    <div class="photo" role="img" aria-label="Pink tulips in a white vase" style="top:38px;width:90px;height:155px;background:radial-gradient(circle at 50% 30%,#f2b7cc,#9cc07a 45%,#eee 65%,#fff 78%)"></div>
    <div class="name" style="top:209px">LOREM IPSUM</div>
    <div class="price" style="top:238px">$25.99</div>
    <div class="btn-pink" style="top:282px;width:80px;height:32px">BUY NOW</div>
  </div>
  <div class="card" style="left:857px;top:1655px;width:225px;height:348px">
    <svg class="ico" style="left:18px;top:16px" width="18" height="16" viewBox="0 0 24 22"><path d="M12 20S2 13.5 2 7.2A5 5 0 0 1 12 5a5 5 0 0 1 10 2.2C22 13.5 12 20 12 20z" fill="none" stroke="#444" stroke-width="1.8"/></svg>
    <svg class="ico" style="left:192px;top:15px" width="20" height="18" viewBox="0 0 24 22"><path d="M2 3h3l3 11h11l3-8H7" fill="none" stroke="#444" stroke-width="1.8"/><circle cx="10" cy="18" r="1.8" fill="#444"/><circle cx="18" cy="18" r="1.8" fill="#444"/></svg>
    <div class="photo" role="img" aria-label="Purple and white tulip bouquet" style="top:40px;width:150px;height:150px;background:radial-gradient(circle at 50% 35%,#e9e3ee,#b98ccc 40%,#4f7a33 62%,#fff 76%)"></div>
    <div class="name" style="top:209px">LOREM IPSUM</div>
    <div class="price" style="top:238px">$25.99</div>
    <div class="btn-pink" style="top:282px;width:80px;height:32px">BUY NOW</div>
  </div>
</section>

<div class="outline-btn">VIEW ALL PRODUCTS</div>

<section>
  <div class="offer-photo" role="img" aria-label="Close-up of blush roses, peach roses and pale berries"></div>
  <h2 class="script abs" style="left:148px;top:2192px;font-size:40px;color:#222">Special offers</h2>
  <div class="sprig" style="left:170px;top:2250px" role="img" aria-label="Leaf sprig ornament"></div>
  <div class="offer" style="width:260px;background:linear-gradient(90deg,var(--peach),#fae3cc)">
    <div class="get">GET</div>
    <div class="rule"></div>
    <h2>25%&nbsp;OFF</h2>
    <p>Lorem Ipsum is simply dummy text of the printing and typesetting.</p>
    <div class="btn">SHOP NOW</div>
  </div>
  <div class="abs" style="left:391px;top:2318px;width:200px;height:312px;background:linear-gradient(90deg,var(--peach),rgba(250,227,204,0))"></div>
</section>

<h2 class="section-title script" style="top:2708px">New Products</h2>
<div class="sprig" style="left:525px;top:2768px" role="img" aria-label="Leaf sprig ornament"></div>

<section>
  <div class="card" style="left:121px;top:2858px;width:225px;height:347px">
    <div class="badge">10%OFF</div>
    <svg class="ico" style="left:193px;top:18px" width="18" height="16" viewBox="0 0 24 22"><path d="M12 20S2 13.5 2 7.2A5 5 0 0 1 12 5a5 5 0 0 1 10 2.2C22 13.5 12 20 12 20z" fill="none" stroke="#444" stroke-width="1.8"/></svg>
    <div class="photo" role="img" aria-label="White and green bouquet with coral ribbon" style="top:40px;width:140px;height:150px;background:radial-gradient(circle at 50% 35%,#eef0c8,#a8c46a 45%,#ec8a6a 60%,#fff 76%)"></div>
    <div class="name" style="top:218px">LOREM IPSUM</div>
    <div class="price" style="top:252px">$25.99<s>$55.99</s></div>
    <div class="btn-pink" style="top:292px;width:99px;height:31px">ADD TO CART</div>
  </div>
  <div class="card" style="left:362px;top:2858px;width:225px;height:347px">
    <div class="badge">15%OFF</div>
    <svg class="ico" style="left:193px;top:18px" width="18" height="16" viewBox="0 0 24 22"><path d="M12 20S2 13.5 2 7.2A5 5 0 0 1 12 5a5 5 0 0 1 10 2.2C22 13.5 12 20 12 20z" fill="none" stroke="#444" stroke-width="1.8"/></svg>
    <div class="photo" role="img" aria-label="Pastel pink mixed bouquet" style="top:38px;width:150px;height:160px;background:radial-gradient(circle at 50% 35%,#f4b8d4,#e7d6e0 40%,#8aa86a 60%,#fff 76%)"></div>
    <div class="name" style="top:218px">LOREM IPSUM</div>
    <div class="price" style="top:252px">$25.99<s>$55.99</s></div>
    <div class="btn-pink" style="top:292px;width:99px;height:31px">ADD TO CART</div>
  </div>
  <div class="card" style="left:603px;top:2858px;width:225px;height:347px">
    <div class="badge">25%OFF</div>
    <svg class="ico" style="left:193px;top:18px" width="18" height="16" viewBox="0 0 24 22"><path d="M12 20S2 13.5 2 7.2A5 5 0 0 1 12 5a5 5 0 0 1 10 2.2C22 13.5 12 20 12 20z" fill="none" stroke="#444" stroke-width="1.8"/></svg>
    <div class="photo" role="img" aria-label="Peach rose bouquet in pink wrap" style="top:40px;width:135px;height:155px;background:radial-gradient(circle at 50% 35%,#f2b6a8,#d98a8a 40%,#6f8a52 60%,#fff 76%)"></div>
    <div class="name" style="top:218px">LOREM IPSUM</div>
    <div class="price" style="top:252px">$25.99<s>$55.99</s></div>
    <div class="btn-pink" style="top:292px;width:99px;height:31px">ADD TO CART</div>
  </div>
  <div class="card" style="left:846px;top:2858px;width:225px;height:347px">
    <div class="badge">50%OFF</div>
    <svg class="ico" style="left:193px;top:18px" width="18" height="16" viewBox="0 0 24 22"><path d="M12 20S2 13.5 2 7.2A5 5 0 0 1 12 5a5 5 0 0 1 10 2.2C22 13.5 12 20 12 20z" fill="none" stroke="#444" stroke-width="1.8"/></svg>
    <div class="photo" role="img" aria-label="Red rose bouquet with red bow" style="top:40px;width:115px;height:155px;background:radial-gradient(circle at 50% 30%,#d4111c,#c2202a 40%,#3e6a2c 62%,#fff 76%)"></div>
    <div class="name" style="top:218px">LOREM IPSUM</div>
    <div class="price" style="top:252px">$25.99<s>$55.99</s></div>
    <div class="btn-pink" style="top:292px;width:99px;height:31px">ADD TO CART</div>
  </div>
</section>

<section class="banner">
  <div class="side" style="left:0" role="img" aria-label="Pink roses and white blossoms"></div>
  <div class="side" style="right:0;background:linear-gradient(180deg,#f3a8b7,#e9708f 50%,#6e8d55)" role="img" aria-label="Pink roses and green leaves"></div>
  <h2>LOREM IPSUM IS SIMPLY DUMMY<br>TEXT OF THE PRINTING AND TYPES<br>ETTING INDUSTRY</h2>
  <div class="btn">SHOP NOW</div>
</section>

<footer class="site-footer">
  <div class="foot-brand"><span>Bloom &amp; Briar</span></div>
  <div class="foot-col" style="left:446px">
    <h4>MENU</h4>
    <ul><li>ARRANGEMENTS</li><li>BOUQUETS</li><li>EVERLASTING ARRANGEMENTS</li><li>GIFTS</li><li>CONTACT</li></ul>
  </div>
  <div class="foot-col" style="left:706px">
    <h4>CONTACT US</h4>
    <div class="contact-row"><span class="circ"><svg width="9" height="12" viewBox="0 0 10 14"><path d="M5 13S1 8 1 5a4 4 0 0 1 8 0c0 3-4 8-4 8z" fill="#555"/><circle cx="5" cy="5" r="1.5" fill="#f3ece8"/></svg></span><span>42 Meadow Lane<br>Fernbrook, VT 05099</span></div>
    <div class="contact-row"><span class="circ"><svg width="10" height="10" viewBox="0 0 12 12"><path d="M2 1l2 0 1 3-1.5 1a7 7 0 0 0 3.5 3.5L8 7l3 1v2c0 1-1 1-1 1C5 11 1 7 1 2c0 0 0-1 1-1z" fill="#555"/></svg></span><span>Call Us<br>555.014.2377</span></div>
    <div class="contact-row"><span class="circ"><svg width="11" height="8" viewBox="0 0 12 9"><rect x="0.5" y="0.5" width="11" height="8" fill="#555"/><path d="M1 1l5 4 5-4" fill="none" stroke="#f3ece8"/></svg></span><span>E mail Us<br>hello@bloombriar.com</span></div>
  </div>
  <div class="foot-col" style="left:970px">
    <h4>FOLLOW US</h4>
    <div class="contact-row"><span class="circ"></span><span>Like us on<br>PETALBOOK</span></div>
    <div class="contact-row"><span class="circ"></span><span>Follow us on<br>CHIRPER</span></div>
    <div class="contact-row"><span class="circ"></span><span>Follow us on<br>LINKWORK</span></div>
  </div>
  <div class="foot-rule"></div>
  <div class="copy">Copyright © 2021 All Rights Reserved</div>
</footer>

</body>
</html>
```